contemporary upscale hair salon

we need a business card design for a modern upscale salon. I would like the card to be vertical, simple, and easy to read. I would like a black matte finish on the info side with white on the back of the card, white lettering with a splash of red incorporated somewhere in there. I also want to incorporate embossing and/or cut out in the letters. The info I would like; Name of the business (Vessa Salon) stylist name (Joan) phone number(5093146620) and web address (www.vessasalon-example.com) I am open to putting shears on the card but without it looking too cheap. Looking for something really modern and edgy. these are just ideas I have, but feel free to show me your creative ideas.
please note: the website is still under construction please do not use any images or colors off the web page. Also i currently do not have a logo, that will be a future project.

```html
<!DOCTYPE html>
<html lang="en">
<head>
<meta charset="utf-8">
<title>Vessa Salon – Business Card</title>
<link href="https://fonts.googleapis.com/css2?family=Pinyon+Script&family=Open+Sans:wght@400;700&display=swap" rel="stylesheet">
<style>
  :root {
    --backdrop: #e6e2dc;
    --card-black: #1c1c1d;
    --card-charcoal: #3a3a3c;
    --card-white: #f4f4f4;
    --hair-grey: #9a9a9a;
    --ink-white: #f2f2f2;
    --accent-red: #d8141f;
  }
  * { margin: 0; padding: 0; box-sizing: border-box; }
  html, body {
    width: 1200px;
    height: 1023px;
    overflow: hidden;
    background: var(--backdrop);
  }
  .canvas {
    position: relative;
    width: 1200px;
    height: 1023px;
    display: flex;
    justify-content: center;
    align-items: center;
    gap: 110px;
  }
  .card {
    position: relative;
    width: 380px;
    height: 665px;
    border-radius: 22px;
    overflow: hidden;
    box-shadow: 0 14px 30px rgba(0,0,0,0.25);
  }

  /* Info side */
  .card--front {
    background: radial-gradient(ellipse at 45% 35%, var(--card-charcoal) 0%, var(--card-black) 75%);
    display: flex;
    flex-direction: column;
    align-items: center;
    text-align: center;
    padding-top: 48px;
  }
  .salon-name {
    font-family: "Pinyon Script", cursive;
    font-weight: 400;
    color: var(--accent-red);
    font-size: 92px;
    line-height: 0.95;
  }
  .salon-name span { display: block; }
  .website {
    font-family: "Pinyon Script", cursive;
    color: var(--ink-white);
    font-size: 24px;
    margin-top: 22px;
  }
  .stylist-label {
    font-family: "Pinyon Script", cursive;
    color: var(--ink-white);
    font-size: 42px;
    margin-top: 30px;
  }
  .stylist-name {
    font-family: "Pinyon Script", cursive;
    color: var(--ink-white);
    font-size: 90px;
    line-height: 1;
    margin-top: 4px;
  }
  .call-label {
    font-family: "Open Sans", sans-serif;
    font-weight: 700;
    color: var(--accent-red);
    font-size: 28px;
    margin-top: 30px;
  }
  .phone {
    font-family: "Open Sans", sans-serif;
    font-weight: 400;
    color: var(--ink-white);
    font-size: 50px;
    letter-spacing: 2px;
    line-height: 1.1;
  }

  /* Back side */
  .card--back {
    background: radial-gradient(ellipse at 80% 70%, var(--card-charcoal) 0%, var(--card-black) 80%);
  }
  .portrait-area {
    position: absolute;
    inset: 0;
    width: 100%;
    height: 100%;
  }
  .back-name {
    position: absolute;
    right: 26px;
    bottom: 70px;
    font-family: "Pinyon Script", cursive;
    font-weight: 400;
    color: var(--accent-red);
    font-size: 54px;
    line-height: 0.95;
    text-align: right;
  }
  .back-name span { display: block; }
  .back-name span + span { margin-right: -14px; }
</style>
</head>
<body>
  <main class="canvas">
    <section class="card card--front" aria-label="Business card, info side">
      <h1 class="salon-name"><span>Vessa</span><span>Salon</span></h1>
      <p class="website">www.vessasalon-example.com</p>
      <p class="stylist-label">Stylist Name:</p>
      <p class="stylist-name">Joan</p>
      <p class="call-label">Call Us:</p>
      <p class="phone">5093146620</p>
    </section>

    <section class="card card--back" aria-label="Business card, back side">
      <svg class="portrait-area" viewBox="0 0 380 665" preserveAspectRatio="none" role="img" aria-label="Black and white illustration of a woman's face framed by long flowing hair">
        <defs>
          <linearGradient id="hair-tone" x1="0" y1="0" x2="1" y2="0.3">
            <stop offset="0" stop-color="var(--card-white)"/>
            <stop offset="0.7" stop-color="#dcdcdc"/>
            <stop offset="1" stop-color="var(--hair-grey)"/>
          </linearGradient>
        </defs>
        <path d="M0 0 H300 C330 120 320 250 270 360 C225 460 235 560 265 665 H0 Z" fill="url(#hair-tone)"/>
      </svg>
      <h2 class="back-name"><span>Vessa</span><span>Salon</span></h2>
    </section>
  </main>
</body>
</html>
```